Powerpoint Deign for a sales presentation

I am looking for a powerpoint presentation design with animations of my Kindle Bright Lantern Method Blueprint
I would like this to be a path that leads from feeling sad to feeling awesome- due to finding your life purpose (your why)

There are 3 main areas that the client needs to know in order to find their why (purpose) Awareness - Intention & Manifest - these should be designed in grey (as this represents the grey miserable world they stay stuck in if they don't have these skills) and each word will need to be animated to come on one at a time

Each of these has 2 solutions that sits under the required steps
Awareness - The Beacon Sharpening Routine & The Lucid Insight Builder
Intention - The T.O.N.E Balance Tuner & The Glowing Tomorrow Glimpse
Manifest - The Lively Horizon Mandate & The Triumphant Spark Method

& a bonus system called The Kestrel Bloom Booster - which can be designed to be shown on a separate slide

These "solutions" should be in colour boxes that compliment our branding of red, white & black or even the orange as shown on the examples
I have a version now - but it has been put together over time & look like it doesn't sit together well, and we have added more along the way.
For example the path goes down rather than up (to success)
There is a sad face at the start & then a happy one - it would be better for the happy one to be at the end
The icons are all ok - but the trampoline one can go

Looking for new ideas and revamped ideas

Target Market(s)

40+ years old (mainly women but not always)

Industry/Entity Type

Personal Development

Other font styles liked:
• Merge

Colors
F0912C
F2A743
F7CA91
FBE8D2
FDF5EE
EB3D1F
EC4F4E
F09395
F8D3D4
FCEDEE

Requirements
Must have
• animation on the power point

```html
<!DOCTYPE html>
<html lang="en">
<head>
<meta charset="utf-8">
<title>Kindle Bright Lantern Method Blueprint</title>
<link rel="stylesheet" href="https://fonts.googleapis.com/css2?family=Fredoka:wght@500;600;700&display=swap">
<style>
  :root {
    --bg: #f2f2f2;
    --ink: #111111;
    --red: #e8303b;
    --orange: #f3941c;
    --grey: #d9d9d9;
    --grey-text: #4d4d4d;
    --green: #00b050;
    --white: #ffffff;
    --peach: #fbe8d2;
  }
  * { box-sizing: border-box; margin: 0; padding: 0; }
  html, body { width: 1200px; height: 675px; overflow: hidden; background: var(--bg); }
  .slide {
    position: relative;
    width: 1200px;
    height: 675px;
    overflow: hidden;
    background: var(--bg);
    font-family: "Fredoka", sans-serif;
  }
  .slide-title {
    position: absolute;
    left: 34px;
    top: 46px;
    width: 300px;
    font-size: 25px;
    line-height: 1.35;
    font-weight: 700;
    color: var(--ink);
  }
  .brand {
    position: absolute;
    left: 1010px;
    top: 48px;
    width: 160px;
    display: flex;
    align-items: center;
    gap: 10px;
    font-size: 28px;
    line-height: 1.05;
    font-weight: 700;
    color: var(--red);
  }
  .brand-dot {
    flex: none;
    width: 18px;
    height: 18px;
    border-radius: 50%;
    background: var(--red);
  }
  .road { position: absolute; left: 0; top: 0; }
  .solution {
    position: absolute;
    display: flex;
    align-items: center;
    justify-content: center;
    text-align: center;
    border-radius: 8px;
    padding: 6px 12px;
    font-size: 20px;
    line-height: 1.35;
    font-weight: 600;
    color: var(--white);
  }
  .solution--awareness { background: var(--red); left: 106px; width: 213px; height: 97px; }
  .solution--intention { background: var(--orange); left: 366px; width: 183px; height: 103px; }
  .solution--manifest { background: var(--grey); color: var(--grey-text); font-weight: 500; left: 605px; width: 183px; height: 96px; }
  .solution--bonus { background: var(--green); left: 983px; top: 362px; width: 183px; height: 103px; }
</style>
</head>
<body>
<main class="slide">
  <h1 class="slide-title">Kindle Bright Lantern Method Blueprint</h1>

  <div class="brand"><span class="brand-dot"></span><span>Kindle Bright</span></div>

  <svg class="road" width="1200" height="675" viewBox="0 0 1280 720" xmlns="http://www.w3.org/2000/svg">
    <g stroke="#e8303b" stroke-width="2">
      <line x1="227" y1="496" x2="227" y2="530"/>
      <line x1="227" y1="378" x2="227" y2="392"/>
    </g>
    <g stroke="#f3941c" stroke-width="2">
      <line x1="487" y1="270" x2="487" y2="286"/>
      <line x1="487" y1="395" x2="487" y2="428"/>
    </g>
    <g stroke="#e8303b" stroke-width="2">
      <line x1="742" y1="191" x2="742" y2="205"/>
      <line x1="742" y1="306" x2="742" y2="328"/>
    </g>

    <g fill="none" stroke-width="74" stroke-linecap="butt">
      <path stroke="#111111" d="M0,660 H290 Q352,660 352,598 V585 Q352,525 400,525"/>
      <path stroke="#f3941c" d="M392,525 H545 Q607,525 607,465"/>
      <path stroke="#d9d9d9" d="M607,467 Q607,405 667,405 H827"/>
      <path stroke="#e8303b" d="M825,405 H850 Q905,405 905,358 Q905,305 960,305 H1022"/>
    </g>
    <polygon fill="#e8303b" points="1015,243 1088,305 1015,368"/>

    <g fill="none" stroke-width="3" stroke-dasharray="12 9">
      <path stroke="#ffffff" d="M0,660 H290 Q352,660 352,598 V585 Q352,525 400,525"/>
      <path stroke="#111111" d="M400,525 H545 Q607,525 607,465 Q607,405 667,405 H827 H850 Q905,405 905,358 Q905,305 960,305 H1040"/>
    </g>

    <g fill="#ffffff">
      <circle cx="227" cy="657" r="30"/>
      <circle cx="490" cy="522" r="30"/>
      <circle cx="743" cy="405" r="30"/>
    </g>
    <g font-family="Fredoka, sans-serif" font-weight="700" font-size="10" fill="#e8303b" text-anchor="middle">
      <text x="227" y="654">Kindle</text><text x="227" y="665">Bright</text>
      <text x="490" y="519">Kindle</text><text x="490" y="530">Bright</text>
      <text x="743" y="402">Kindle</text><text x="743" y="413">Bright</text>
    </g>

    <path fill="#f3941c" d="M75,622 L47,590 A42,42 0 1 1 103,590 Z"/>
    <circle cx="75" cy="556" r="31" fill="#ffffff"/>
    <circle cx="75" cy="556" r="27" fill="#fbe8d2" role="img" aria-label="Portrait of a sad woman at the start of the path"/>

    <path fill="#f3941c" d="M1140,368 L1112,336 A42,42 0 1 1 1168,336 Z"/>
    <circle cx="1140" cy="302" r="31" fill="#ffffff"/>
    <circle cx="1140" cy="302" r="27" fill="#fbe8d2" role="img" aria-label="Portrait of a happy woman at the end of the path"/>

    <g transform="translate(227,567)">
      <path d="M-18,0 Q0,-16 18,0 Q0,16 -18,0 Z" fill="#111111"/>
      <circle r="7" fill="#ffffff"/>
      <circle r="4" fill="#111111"/>
      <g stroke="#111111" stroke-width="2.5" stroke-linecap="round">
        <line x1="0" y1="-14" x2="0" y2="-20"/>
        <line x1="-9" y1="-12" x2="-12" y2="-18"/>
        <line x1="9" y1="-12" x2="12" y2="-18"/>
        <line x1="-17" y1="-8" x2="-22" y2="-13"/>
        <line x1="17" y1="-8" x2="22" y2="-13"/>
      </g>
    </g>
    <text x="225" y="611" text-anchor="middle" font-family="Fredoka, sans-serif" font-weight="600" font-size="26" fill="#111111">Awareness</text>

    <g transform="translate(410,452)">
      <path d="M-14,20 V8 Q-20,4 -18,-4 Q-16,-20 2,-20 Q18,-20 18,-4 L22,4 L17,6 V12 Q17,16 10,16 V20 Z" fill="#111111"/>
      <circle cx="2" cy="-5" r="9" fill="#ffffff"/>
      <text x="2" y="0" text-anchor="middle" font-family="Fredoka, sans-serif" font-weight="700" font-size="14" fill="#111111">?</text>
    </g>
    <text x="440" y="464" font-family="Fredoka, sans-serif" font-weight="600" font-size="26" fill="#111111">Intention</text>

    <g transform="translate(657,345)">
      <circle cx="0" cy="-4" r="6" fill="#111111"/>
      <path d="M-14,-18 Q-14,6 0,10 Q14,6 14,-18" fill="none" stroke="#111111" stroke-width="5" stroke-linecap="round"/>
      <path d="M-6,8 V20 H6 V8 Z" fill="#111111"/>
      <path d="M0,-26 L2,-21 L7,-21 L3,-18 L5,-13 L0,-16 L-5,-13 L-3,-18 L-7,-21 L-2,-21 Z" fill="#111111"/>
    </g>
    <text x="688" y="357" font-family="Fredoka, sans-serif" font-weight="600" font-size="26" fill="#111111">Manifest</text>
  </svg>

  <div class="solution solution--awareness" style="top:258px">The Beacon Sharpening Routine</div>
  <div class="solution solution--awareness" style="top:367px">The Lucid Insight Builder</div>

  <div class="solution solution--intention" style="top:150px">The T.O.N.E Balance Tuner</div>
  <div class="solution solution--intention" style="top:267px">The Glowing Tomorrow Glimpse</div>

  <div class="solution solution--manifest" style="top:83px">The Lively Horizon Mandate</div>
  <div class="solution solution--manifest" style="top:191px">The Triumphant Spark Method</div>

  <div class="solution solution--bonus">Bonus Kestrel Bloom Booster</div>
</main>
</body>
</html>
```